Landscaping Contract with customizable fillable form

Need a PDF Template with a format that can be filled in with info by us. Then sent to the customer for signature. form need to be able to be changed for each customer

Industry/Entity Type

Landscaping

Colors
00AB8E
00BBA5
67D7C9
C6EFE9
E9F9F6

```html
<!DOCTYPE html>
<html lang="en">
<head>
<meta charset="UTF-8">
<title>Estate Turf Program</title>
<link href="https://fonts.googleapis.com/css2?family=Arimo:wght@400;700&family=Poppins:wght@800&display=swap" rel="stylesheet">
<style>
  :root{
    --green:#16661c;
    --band:#e5ebe7;
    --rule:#b7d6cb;
    --ink:#2f2f2f;
    --paper:#ffffff;
  }
  *{box-sizing:border-box;margin:0;padding:0}
  html,body{width:1200px;height:1200px;overflow:hidden;background:var(--paper)}
  body{font-family:"Arimo",Arial,sans-serif;color:var(--ink);position:relative}
  .brand{position:absolute;left:138px;top:120px;display:flex;align-items:center;gap:14px}
  .brand-dot{width:64px;height:64px;border-radius:50%;border:5px solid var(--green)}
  .brand-name{font-size:24px;font-weight:700;color:var(--green)}
  .contact{position:absolute;left:762px;top:100px}
  .contact-name{font-weight:700;font-size:21px;color:#111;margin-left:33px;margin-bottom:38px}
  .contact-line{display:flex;align-items:center;gap:9px;font-size:22px;color:#111;height:35px}
  .contact-line svg{width:26px;height:26px;flex:none}
  .title-band{position:absolute;left:134px;top:272px;width:932px;height:58px;background:var(--band);
    display:flex;align-items:center;justify-content:center}
  .title-band h1{font-family:"Poppins",sans-serif;font-weight:800;font-size:40px;letter-spacing:1.5px;color:var(--green);line-height:1;padding-top:6px}
  .turf-table{position:absolute;left:134px;top:335px;width:932px;border-collapse:collapse;font-size:13.3px;line-height:17.5px;table-layout:fixed}
  .turf-table th{background:var(--green);color:#fff;font-weight:400;height:21px;padding:0 6px;text-align:center}
  .turf-table th.col-service{text-align:left}
  .turf-table td{border:1px solid var(--rule);padding:2px 6px 1px;vertical-align:top}
  .turf-table td.desc{text-align:justify}
  .turf-table td.dates{text-align:center}
  .turf-table td.dates.mid{vertical-align:middle}
</style>
</head>
<body>
  <div class="brand">
    <span class="brand-dot"></span>
    <span class="brand-name">Greenfield Grounds</span>
  </div>

  <div class="contact">
    <div class="contact-name">Dana Whitfield</div>
    <div class="contact-line">
      <svg viewBox="0 0 26 26"><circle cx="13" cy="13" r="12" fill="none" stroke="#3d8a55" stroke-width="1"/><path d="M9 7.5c1 0 1.6 2.4 1.6 3 0 .8-1 1-1 1.6.4 1.6 2.2 3.5 3.8 3.9.6 0 .9-1 1.6-1 .7 0 3 .7 3 1.6 0 1.2-1 2.2-2.2 2.2C11.5 18.8 7 14.2 7 9.9 7 8.5 8 7.5 9 7.5z" fill="none" stroke="#3d8a55" stroke-width="1"/></svg>
      <span>555-204-7731</span>
    </div>
    <div class="contact-line">
      <svg viewBox="0 0 26 26"><circle cx="13" cy="13" r="12" fill="none" stroke="#3d8a55" stroke-width="1"/><rect x="7" y="9" width="12" height="8.5" fill="none" stroke="#3d8a55" stroke-width="1"/><path d="M7 9l6 5 6-5" fill="none" stroke="#3d8a55" stroke-width="1"/></svg>
      <span>hello@greenfieldgrounds.com</span>
    </div>
  </div>

  <div class="title-band"><h1>ESTATE TURF PROGRAM</h1></div>

  <table class="turf-table">
    <colgroup><col style="width:142px"><col style="width:526px"><col style="width:156px"><col style="width:108px"></colgroup>
    <thead>
      <tr><th class="col-service">Service</th><th>Description</th><th>Dates</th><th>Price</th></tr>
    </thead>
    <tbody>
      <tr><td>Early Spring</td><td class="desc">Complete, granular fertilizer and pre-emergant crabgrass control</td><td class="dates">April 1 - April 22</td><td></td></tr>
      <tr><td>Spring</td><td class="desc">Complete, granular fertilizer with iron and broadleaf control</td><td class="dates">April 23 - May 13</td><td></td></tr>
      <tr><td>Early Summer</td><td class="desc">Complete, granular fertilizer with iron and broadleaf control</td><td class="dates">June 4 - June 24</td><td></td></tr>
      <tr><td>Late Summer</td><td class="desc">Post-emergent crabgrass and late summer weed control</td><td class="dates">June 16 - Aug 5</td><td></td></tr>
      <tr><td>Early Fall</td><td class="desc">Complete balanced fertilizer with iron and weed control</td><td class="dates">Aug 20 - Sept 9</td><td></td></tr>
      <tr><td>Late Fall</td><td class="desc">Granular Fertilizer w/ high potassium to winterize lawn</td><td class="dates">Oct 1 - Oct 31</td><td></td></tr>
      <tr><td>Aeration</td><td class="desc">Due to the constant compatcion of soil from mowing and foot traffic, we recommend a yearly aeration of the lawn. It helps get nutrients, water and air down to the roots of the soil. Creates strong root growth. Vital Service for a superior lawn.</td><td class="dates mid">Aug 20 - Oct 15</td><td></td></tr>
      <tr><td>Grub Control</td><td class="desc">Highly effective, prevenative treatment for grub control.</td><td class="dates">Mid Summer</td><td></td></tr>
      <tr><td>Lime</td><td class="desc">Essential application to maintain proper PH of soil.</td><td class="dates">Early Spring or Late fall</td><td></td></tr>
      <tr><td>Fungicide</td><td class="desc">Prevantive and curative treatment for various turf diseases.</td><td class="dates">Throughout season</td><td></td></tr>
      <tr><td>Nutsedge</td><td class="desc">Highly effective treatment for nutsedge (Fast growing, unsightly yellow weed)</td><td class="dates">Mid Summer</td><td></td></tr>
      <tr><td>Bentgrass</td><td class="desc">Specialty Application for treatment of unsightly spreading creeping bentgrass.</td><td class="dates"></td><td></td></tr>
      <tr><td>Slit-Seeding</td><td class="desc">Guarenteed method of slicing the soil to sew new seed directly into soil. Custom seed blend specific to your property. Done in a crisscross patternt for complete coverage.</td><td class="dates"></td><td></td></tr>
      <tr><td>Overseeding</td><td class="desc">Broadcast method of incorporating seed immediatly after coreaeration to replenish old lawn with new seedlings. Recommended yearly.</td><td class="dates"></td><td></td></tr>
      <tr><td>Soil Samples</td><td class="desc">Essential service, provides us with lab results of soil structure to effectively bring soil to proper allignement.</td><td class="dates"></td><td></td></tr>
    </tbody>
  </table>
</body>
</html>
```